Beekeeper needs box/label design for honey/CBD and other honey-related products

We need a box (or label) design for a beekeeping company in Virginia called Tamsin Hollow Farm. Our products will include honey mixed with CBD oil and other essential oils (vanilla, lavender, etc).The box design should be scalable to include several different honey/oil products. We would like to incorporate our current farm logo into the design. Here is a link to a honey producing company with a series of products using their honey mixed with certain oils. It's a good reference of what type box/label design we would like (https://corbinandlyle.co/pages/honey).

Target Market(s)

Retail stores and consumers

Requirements
Must have
• Tamsin Hollow Farm name and logo

```html
<!DOCTYPE html>
<html lang="en">
<head>
<meta charset="utf-8">
<title>Tamsin Hollow Farm – CBD Honey Oil Labels</title>
<link rel="stylesheet" href="https://fonts.googleapis.com/css2?family=Cinzel:wght@400&family=Libre+Baskerville:wght@700&family=Yellowtail&family=Arimo:wght@400&display=swap">
<style>
  :root {
    --page: #f4f1ea;
    --ink-grey: #4a4a4a;
    --olive: #5e5a1e;
    --leaf-green: #1f7a2a;
    --label-white: #f1f2ee;
    --label-green: #5cb82e;
    --cream: #f3e9d6;
    --gold-band: #b9a747;
    --gold-band-dark: #a59434;
    --brown-text: #5a4a1c;
    --white: #ffffff;
    --spec-dark: #1d2a12;
    --tag-grey: #6c7a5c;
  }
  * { box-sizing: border-box; margin: 0; padding: 0; }
  html, body { width: 1200px; height: 799px; overflow: hidden; }
  body { background: var(--page); font-family: "Arimo", Arial, sans-serif; }

  .canvas { position: relative; width: 1200px; height: 799px; }

  .option-title {
    position: absolute; top: 64px; width: 318px;
    text-align: center; font-size: 22px; color: var(--ink-grey); letter-spacing: 0.5px;
  }
  .option-title--one { left: 254px; }
  .option-title--two { left: 478px; }

  .label {
    position: absolute; top: 242px; width: 318px; height: 393px; overflow: hidden;
    box-shadow: 0 2px 10px rgba(0,0,0,0.12);
  }
  .label--green {
    left: 185px;
    background: linear-gradient(180deg, var(--label-white) 0%, var(--label-white) 28%, #d9ebc3 55%, var(--label-green) 100%);
  }
  .label--honey { left: 563px; background: var(--cream); }

  .brand { position: absolute; left: 0; right: 0; text-align: center; }
  .brand-mark {
    display: block; margin: 0 auto 14px; width: 44px; height: 44px;
    border: 3px solid var(--olive);
  }
  .brand-name {
    font-family: "Cinzel", "Times New Roman", serif; font-weight: 400;
    font-size: 20px; line-height: 1; color: var(--olive); letter-spacing: 1px;
    white-space: nowrap;
  }
  .label--green .brand { top: 70px; }
  .label--honey .brand { top: 38px; }

  .product-name {
    position: absolute; left: 0; right: 0; text-align: center;
    font-family: "Libre Baskerville", Georgia, serif; font-weight: 700; font-size: 20px;
    line-height: 1;
  }
  .label--green .product-name { top: 206px; color: var(--leaf-green); }
  .label--honey .product-name { top: 288px; color: var(--brown-text); }

  .illustration { position: absolute; border-radius: 4px; }
  .illustration--bees {
    left: 116px; top: 240px; width: 160px; height: 120px;
    background: linear-gradient(135deg, #3f7a2c 0%, #7fae3e 40%, #f0c230 75%, #d99a1c 100%);
  }
  .illustration--jars {
    left: 56px; top: 150px; width: 206px; height: 124px;
    background: linear-gradient(135deg, #4d7a34 0%, #c98a2a 45%, #f0a21a 70%, #f4c44a 100%);
  }

  .tagline {
    position: absolute; left: 60px; top: 318px;
    font-size: 10px; line-height: 1.2; color: var(--tag-grey); text-transform: uppercase;
  }

  .spec { position: absolute; font-size: 11px; line-height: 1; color: var(--spec-dark); }
  .label--green .spec--volume { left: 60px; top: 370px; }
  .label--green .spec--strength { right: 36px; top: 370px; }

  .spectrum-band {
    position: absolute; left: 0; right: 0; top: 312px; bottom: 0;
    background: linear-gradient(180deg, var(--gold-band) 0%, var(--gold-band-dark) 100%);
  }
  .spectrum-name {
    position: absolute; left: 0; right: 0; top: 26px; text-align: center;
    font-family: "Yellowtail", cursive; font-size: 17px; line-height: 1; color: var(--white);
  }
  .label--honey .spec { color: var(--white); font-size: 13px; top: 56px; }
  .label--honey .spec--volume { left: 64px; }
  .label--honey .spec--strength { right: 44px; }
</style>
</head>
<body>
<main class="canvas">
  <p class="option-title option-title--one">OPTION-1</p>
  <p class="option-title option-title--two">OPTION-2</p>

  <section class="label label--green" aria-label="Option 1 label">
    <div class="brand">
      <span class="brand-mark"></span>
      <p class="brand-name">Tamsin Hollow Farm</p>
    </div>
    <h2 class="product-name">CBD HONEY OIL</h2>
    <div class="illustration illustration--bees" role="img" aria-label="Hemp leaves, honeycomb and two honey bees"></div>
    <p class="tagline">Premium<br>Quality</p>
    <span class="spec spec--volume">30mL.</span>
    <span class="spec spec--strength">1000MG</span>
  </section>

  <section class="label label--honey" aria-label="Option 2 label">
    <div class="brand">
      <span class="brand-mark"></span>
      <p class="brand-name">Tamsin Hollow Farm</p>
    </div>
    <div class="illustration illustration--jars" role="img" aria-label="Honey jars with a spoon, hemp leaf, clover and daisies"></div>
    <h2 class="product-name">CBD HONEY OIL</h2>
    <div class="spectrum-band">
      <p class="spectrum-name">Full Spectrum</p>
      <span class="spec spec--volume">30mL.</span>
      <span class="spec spec--strength">1000MG</span>
    </div>
  </section>
</main>
</body>
</html>
```